Covid 19 Exit Strategy one page brochure

I would like to design, and will need URGENT help, a brochure detailing a Covid 19 Exit Strategy plan. This brochure will need to be understood easily and the graphics inside should make it easy for people to understand without reading the entire text. This project is quite urgent and needs to be completed THIS WEEK - by Saturday may 16th at the latest. I am attaching two examples. I will provide the text.

```html
<!DOCTYPE html>
<html lang="en">
<head>
<meta charset="utf-8">
<title>Covid-19 Exit Strategy Brochure</title>
<link rel="stylesheet" href="https://fonts.googleapis.com/css2?family=Montserrat:wght@800;900&family=Open+Sans:wght@400;600;700&family=Oswald:wght@500;600&display=swap">
<style>
  :root{
    --header-black:#161616;
    --navy:#0f2547;
    --navy-deep:#0b1930;
    --navy-light:#1d3f72;
    --red:#e02020;
    --sky:#45a3dc;
    --white:#ffffff;
    --muted:#9aa8bf;
  }
  *{margin:0;padding:0;box-sizing:border-box}
  html,body{width:686px;height:1200px;overflow:hidden;background:var(--navy-deep)}
  .brochure{position:relative;width:686px;height:1200px;overflow:hidden;
    font-family:"Open Sans",Arial,sans-serif;color:var(--white);
    background:var(--navy)}
  .masthead{position:absolute;left:0;top:0;width:100%;height:225px;background:var(--header-black)}
  .masthead__block{position:absolute;left:160px;top:40px}
  .masthead__kicker{font-weight:600;font-size:25px;letter-spacing:.3px;line-height:1}
  .masthead__title{font-family:"Montserrat",sans-serif;font-weight:900;font-size:76px;line-height:1;margin-top:6px;letter-spacing:-1px}
  .masthead__title span{color:var(--red)}
  .masthead__sub{font-weight:600;font-size:23px;line-height:1;margin-top:8px}

  .content{position:absolute;left:0;top:225px;width:100%;height:805px;
    background:radial-gradient(circle at 50% 52%, var(--navy-light) 0%, var(--navy) 45%, var(--navy-deep) 100%)}
  .content__backdrop{position:absolute;left:30px;top:40px;width:626px;height:620px;border-radius:50%;
    background:radial-gradient(circle, rgba(60,100,160,.25) 0%, rgba(15,37,71,0) 70%)}
  .strategy-title{position:absolute;top:32px;width:100%;text-align:center;
    font-family:"Montserrat",sans-serif;font-weight:900;font-size:33px}
  .strategy-tag{position:absolute;left:133px;top:105px;width:420px;height:60px;background:var(--red);
    display:flex;align-items:center;justify-content:center;font-weight:700;font-size:19px}
  .objective{position:absolute;left:86px;top:190px;width:530px;font-size:17.5px;line-height:1.45}
  .objective b{font-weight:700}

  .step{position:absolute;width:180px;font-size:11.5px;line-height:1.5;text-align:justify}
  .step__num{font-family:"Oswald",sans-serif;font-weight:600;font-size:38px;color:var(--sky);line-height:1;display:block;margin-bottom:4px}
  .step--left .step__num{text-align:right}
  .step--left{left:59px}
  .step--right{left:449px}

  .icon{position:absolute;border-radius:6px;background:rgba(255,255,255,.85)}
  .icon--round{border-radius:50%}
  .connectors{position:absolute;left:0;top:0}

  .footer-band{position:absolute;left:0;top:1030px;width:100%;height:78px}
  .footer-band__hashtag{position:absolute;left:58px;top:22px}
  .footer-band__hashtag strong{display:block;font-size:17px;font-weight:700}
  .footer-band__hashtag small{display:block;font-size:9px;font-weight:700;margin-top:2px}
  .footer-band__contact{position:absolute;left:420px;top:18px;font-size:13px;font-weight:600;line-height:1.7}
  .footer-band__contact div{display:flex;align-items:center;gap:8px}

  .signature{position:absolute;left:0;top:1108px;width:100%;height:92px;background:var(--navy-deep)}
  .signature__mark{position:absolute;left:254px;top:38px;width:14px;height:14px;background:var(--red)}
  .signature__rule{position:absolute;left:288px;top:26px;width:1px;height:40px;background:var(--muted)}
  .signature__name{position:absolute;left:298px;top:36px;font-size:9px;letter-spacing:1px;color:var(--muted);text-transform:uppercase;line-height:1.4}
</style>
</head>
<body>
<main class="brochure">
  <header class="masthead">
    <div class="masthead__block">
      <p class="masthead__kicker">CORONAVIRUS</p>
      <h1 class="masthead__title">COVID-<span>19</span></h1>
      <p class="masthead__sub">INFORMATION AND GUIDELINES</p>
    </div>
  </header>

  <section class="content">
    <div class="content__backdrop" role="img" aria-label="Faint globe held in hands, dark blue"></div>
    <h2 class="strategy-title">THE EXIT STRATEGY</h2>
    <div class="strategy-tag">WHAT DOES THE STRATEGY CONSIST OF?</div>
    <p class="objective"><b>Objective</b>: To gradually phase out the restrictions imposed to curb the spread of the coronavirus while remaining cautions.</p>

    <svg class="connectors" width="686" height="805" viewBox="0 0 686 805" fill="none" stroke="#c9d3e3" stroke-width="1" stroke-dasharray="3 3">
      <path d="M345 300 H390 V340"/>
      <path d="M390 355 H298 V385"/>
      <path d="M345 400 H380 V460"/>
      <path d="M380 470 H298 V555"/>
      <path d="M350 580 H395 V600"/>
    </svg>

    <div class="icon" style="left:267px;top:280px;width:80px;height:78px" role="img" aria-label="Hospital building icon with red cross"></div>
    <div class="icon" style="left:355px;top:360px;width:60px;height:62px" role="img" aria-label="House icon with red alert badge"></div>
    <div class="icon icon--round" style="left:262px;top:415px;width:64px;height:64px" role="img" aria-label="Magnifying glass over chart icon with red tick"></div>
    <div class="icon" style="left:365px;top:480px;width:60px;height:62px" role="img" aria-label="Row of test tubes icon"></div>
    <div class="icon" style="left:270px;top:560px;width:64px;height:74px" role="img" aria-label="Group of standing figures icon with distance circle"></div>
    <div class="icon" style="left:355px;top:625px;width:72px;height:52px" role="img" aria-label="Vulnerable group figures icon"></div>

    <div class="step step--left" style="top:297px"><span class="step__num">01</span>Ensure, at all times, sufficient hospital capacities.</div>
    <div class="step step--right" style="top:337px"><span class="step__num">02</span>Foreesee the posibility of reintroducing stricter measures in the event of a strong resurgence of the virus among the population.</div>
    <div class="step step--left" style="top:437px"><span class="step__num">03</span>Provide close monitoring of the evolution of the pandemic during the entire exit, as well as the secondary effectsof the confinement.</div>
    <div class="step step--right" style="top:506px"><span class="step__num">04</span>Foster testing capacities and support research in particular with regard to test to measured the aquried immunity of the population.</div>
    <div class="step step--left" style="top:606px"><span class="step__num">05</span>Apply basic barrier gestures and reinforce them with other specific measures, including in the workplace , to minimise the risk of an uncontrolled spread of the virus.</div>
    <div class="step step--right" style="top:680px"><span class="step__num">06</span>Protect, in particular, vulnerable groups.</div>
  </section>

  <div class="footer-band">
    <svg width="686" height="78" viewBox="0 0 686 78" style="position:absolute;left:0;top:0">
      <rect width="686" height="78" fill="var(--sky)"/>
      <polygon points="0,0 365,0 330,78 0,78" fill="var(--white)"/>
      <polygon points="0,0 345,0 310,78 0,78" fill="var(--red)"/>
    </svg>
    <div class="footer-band__hashtag"><strong>#STAYSAFEHOME</strong><small>DON'T HAVE TO GO OUTSIDE? PLEASE STAY AT HOME</small></div>
    <div class="footer-band__contact">
      <div><svg width="12" height="12" viewBox="0 0 12 12" fill="none" stroke="#0b1930" stroke-width="1.2"><circle cx="6" cy="6" r="5"/><path d="M1 6h10M6 1c2 2 2 8 0 10M6 1c-2 2-2 8 0 10"/></svg>www.exitplan-info.org</div>
      <div><svg width="12" height="12" viewBox="0 0 12 12"><circle cx="6" cy="6" r="6" fill="#0b1930"/><path d="M4 3.5l1 1.5-.6.7c.4.9 1 1.5 1.9 1.9l.7-.6 1.5 1-.6 1c-2.5-.3-4.5-2.3-4.8-4.8z" fill="#fff"/></svg>0800- 4120</div>
    </div>
  </div>

  <footer class="signature">
    <span class="signature__mark"></span>
    <span class="signature__rule"></span>
    <p class="signature__name">Conseil National<br>de Santé Publique</p>
  </footer>
</main>
</body>
</html>
```